New Brochure for existing Virtual Reality Amusement Arena

I need a two sided half page brochure for my arcade. it needs to say what we do and what we have to offer. It basically needs to be a paper copy of all the information thats on my website www.verbomix-arena.com
Please check that as it is very informative!
Industry/Entity Type
Entertainment
Colors
Designer to choose colors to be used in the design.
Requirements
Must have
- Color. I have uploaded an old brochure I had made, but now we have a new company and new logo, please make it similar to that. Please pull all pics from my website www.verbomix-arena.com
Should not have
- useless information

```html
<!DOCTYPE html>
<html lang="en">
<head>
<meta charset="utf-8">
<title>Verbomix Arena – Bi-Fold Brochure Inside</title>
<link rel="stylesheet" href="https://fonts.googleapis.com/css2?family=Lato:wght@300;400;700;900&family=Rubik:wght@400;800&display=swap">
<style>
  :root {
    --page: #ffffff;
    --ink: #3a3a3a;
    --muted: #5a5a5a;
    --fog-top: #e9ebf1;
    --fog-bottom: #dfe4f2;
    --night-1: #1e2a6e;
    --night-2: #3b3f9a;
    --night-3: #5b5fc0;
    --band: rgba(40, 50, 140, 0.55);
    --accent: #1f8fe0;
    --box-line: #3aa2f0;
    --white: #ffffff;
    --hex-ring: #5d62b8;
    --hex-fill: #9a9aa0;
  }
  * { box-sizing: border-box; margin: 0; padding: 0; }
  html, body { width: 1200px; height: 1021px; overflow: hidden; background: var(--page); }
  body { position: relative; font-family: "Lato", sans-serif; color: var(--ink); }

  .brochure { position: absolute; left: 46px; top: 117px; width: 1105px; height: 781px; overflow: hidden; }

  .features {
    position: absolute; left: 0; top: 0; width: 351px; height: 781px;
    background: linear-gradient(180deg, var(--fog-top) 0%, #f3f4f8 40%, var(--fog-bottom) 100%);
    border: 1px solid #d6dae6;
  }
  .feature { position: absolute; left: 20px; width: 311px; text-align: center; }
  .feature__icon { display: block; margin: 0 auto 2px; width: 30px; height: 30px; }
  .feature__title { font-weight: 700; font-size: 25px; color: var(--ink); line-height: 1.1; margin-bottom: 5px; }
  .feature__text { font-size: 10.4px; line-height: 1.43; color: var(--muted); }

  .hero {
    position: absolute; left: 351px; top: 0; width: 754px; height: 781px;
    background:
      radial-gradient(ellipse at 55% 45%, #a0333a 0%, rgba(160,51,58,0) 22%),
      radial-gradient(ellipse at 40% 70%, var(--night-3) 0%, rgba(91,95,192,0) 55%),
      linear-gradient(160deg, var(--night-1) 0%, var(--night-2) 55%, #2a2f7c 100%);
  }
  .hero__band { position: absolute; left: 0; top: 0; width: 202px; height: 781px; background: var(--band); }

  .brand { position: absolute; left: 38px; top: 42px; display: flex; align-items: center; gap: 10px; }
  .brand__dot { width: 36px; height: 36px; border-radius: 50%; background: var(--white); }
  .brand__name { font-family: "Lato", sans-serif; font-weight: 900; font-size: 30px; letter-spacing: 2px; color: var(--white); }

  .tagline { position: absolute; left: 16px; top: 218px; color: var(--white); font-family: "Rubik", sans-serif; text-align: center; width: 180px; }
  .tagline__main { font-size: 30px; font-weight: 800; line-height: 1; }
  .tagline__main span { font-weight: 400; font-size: 20px; }
  .tagline__sub { font-size: 13px; font-weight: 400; letter-spacing: 0.5px; margin-top: 2px; }
  .tagline__sub strong { font-weight: 800; font-size: 15px; }

  .fees { position: absolute; left: 456px; top: 34px; width: 290px; color: var(--white); text-align: center; }
  .fees__title { font-size: 23px; font-weight: 300; letter-spacing: 0.5px; line-height: 1; }
  .fees__title strong { font-weight: 900; }
  .fees__note { font-size: 12px; margin-top: 3px; }
  .fees__boxes { display: flex; justify-content: center; gap: 13px; margin-top: 8px; }
  .fee-box { position: relative; width: 115px; height: 88px; border: 1px solid var(--box-line); padding-top: 6px; }
  .fee-box::before { content: ""; position: absolute; left: 0; top: 0; border-top: 16px solid var(--accent); border-right: 16px solid transparent; }
  .fee-box__label { font-size: 14px; }
  .fee-box__price { font-size: 27px; font-weight: 900; line-height: 1.15; }
  .fee-box__unit { font-size: 14px; }
  .fees__info { font-size: 11px; line-height: 1.5; margin-top: 12px; padding: 0 4px; }

  .photo-slot { position: absolute; }
  .photo-slot--a { left: 581px; top: 427px; width: 170px; height: 190px; }
  .photo-slot--b { left: 459px; top: 560px; width: 202px; height: 221px; }
</style>
</head>
<body>
  <main class="brochure">
    <section class="features">
      <article class="feature" style="top:22px">
        <svg class="feature__icon" viewBox="0 0 30 30" fill="none" stroke="#444" stroke-width="1.6" stroke-linecap="round" stroke-linejoin="round"><circle cx="19" cy="5" r="2.5"/><path d="M9 11l5-3 5 2 2 5 4 1M15 9l-3 8 5 4-2 7M12 17l-4 4H4"/></svg>
        <h2 class="feature__title">Immersive VR</h2>
        <p class="feature__text">Powered by Stridex Motion, we have Tampa’s only fully immersive VR. These machines allow you to walk inside virtual reality. When you walk in real life, you walk in the game. The game selection is limited, but the experience is the most unique.</p>
      </article>
      <article class="feature" style="top:178px">
        <svg class="feature__icon" viewBox="0 0 30 30" fill="none" stroke="#444" stroke-width="1.6" stroke-linecap="round" stroke-linejoin="round"><path d="M15 3v7"/><rect x="4" y="10" width="22" height="14" rx="3"/><path d="M9 15v4M7 17h4"/><circle cx="20" cy="16" r="0.8"/><circle cx="22" cy="19" r="0.8"/></svg>
        <h2 class="feature__title">Nova Play</h2>
        <p class="feature__text">The gold standard in VR made by Halcyn. This has the best selection of games, and the most fun in our opinion. A great variety of multiplayer and single player games, for kids and adults, this is fun for all ages. We currently have two of these stations allowing two to link up and play together or by yourself.</p>
      </article>
      <article class="feature" style="top:370px">
        <svg class="feature__icon" viewBox="0 0 30 30" fill="none" stroke="#444" stroke-width="1.6" stroke-linecap="round" stroke-linejoin="round"><path d="M5 24V17a10 10 0 0 1 20 0v7z"/><path d="M5 20h-2v5h2M11 17h14"/></svg>
        <h2 class="feature__title">Seated VR</h2>
        <p class="feature__text">For both the relaxed individual who isn’t familiar with video games, and the in-depth everyday gamer, these stations are great for both. We have selections that allow you to experience a different world with hardly any effort, and the advanced campaign based games that come with a Zentro controller. This is a terrific station for gamers and non-gamers alike.</p>
      </article>
      <article class="feature" style="top:573px">
        <svg class="feature__icon" viewBox="0 0 30 30" fill="none" stroke="#444" stroke-width="1.6" stroke-linecap="round" stroke-linejoin="round"><circle cx="19" cy="5" r="2.5"/><path d="M9 11l5-3 5 2 2 5 4 1M15 9l-3 8 5 4-2 7M12 17l-4 4H4"/></svg>
        <h2 class="feature__title">Free Roam VR</h2>
        <p class="feature__text">Completely wireless, walk and move freely in your space with a top of the line Kestrel laptop strapped to your back. This is the way virtual reality was meant to be played, with no restrictions. Feel and move like a soldier shooting a rifle, jump off walls and wield swords like a ninja, this is our most realistic experience yet.</p>
      </article>
    </section>

    <section class="hero" role="img" aria-label="Player in a red shirt wearing a VR headset, holding two blaster controllers in blue haze">
      <div class="hero__band"></div>

      <div class="brand">
        <span class="brand__dot"></span>
        <span class="brand__name">VERBOMIX ARENA</span>
      </div>

      <div class="tagline">
        <p class="tagline__main">GAMING <span>LIKE</span></p>
        <p class="tagline__sub">YOU’VE <strong>NEVER SEEN</strong></p>
      </div>

      <div class="fees">
        <p class="fees__title">ENTRY <strong>FEE</strong></p>
        <p class="fees__note">DealDrop rate</p>
        <div class="fees__boxes">
          <div class="fee-box">
            <p class="fee-box__label">1 person 2 hour</p>
            <p class="fee-box__price">$45</p>
            <p class="fee-box__unit">per person</p>
          </div>
          <div class="fee-box">
            <p class="fee-box__label">2 person 2 hour</p>
            <p class="fee-box__price">$40</p>
            <p class="fee-box__unit">per person</p>
          </div>
        </div>
        <p class="fees__info">Just walk right in. Up to eight people can enter at once at stay to try all our products. A new group comes in every 2 hours.</p>
      </div>

      <svg class="photo-slot photo-slot--a" viewBox="0 0 170 190" role="img" aria-label="Black and white photo of a guest playing with a VR headset and controllers">
        <polygon points="85,2 168,49 168,141 85,188 2,141 2,49" fill="none" stroke="var(--hex-ring)" stroke-width="4" opacity="0.8"/>
        <polygon points="85,12 159,54 159,136 85,178 11,136 11,54" fill="#b8b8bc"/>
      </svg>
      <svg class="photo-slot photo-slot--b" viewBox="0 0 202 221" role="img" aria-label="Photo of a player in a grey shirt wearing a VR headset holding two controllers">
        <polygon points="101,2 200,57 200,164 101,219 2,164 2,57" fill="#1c2160" stroke="var(--hex-ring)" stroke-width="3"/>
        <polygon points="101,14 189,63 189,158 101,207 13,158 13,63" fill="var(--hex-fill)"/>
      </svg>
    </section>
  </main>

  <footer>
    <p style="position:absolute;left:46px;top:962px;font-size:18px;font-weight:300;color:#555;">A4 Size</p>
    <p style="position:absolute;left:0;width:1200px;top:948px;text-align:center;font-size:44px;font-weight:300;color:#333;line-height:1;">INSIDE</p>
    <p style="position:absolute;right:48px;top:962px;font-size:18px;font-weight:300;color:#555;">Bi-Fold Brochure</p>
  </footer>
</body>
</html>
```